Priority Goals poster for school year

We are an elementary school and the past two years have had you help us to design a "poster" that illustrates our goal of the coming year. I am attaching our last year's one, along with some photos of our (ver rough) thinking for next years. The priority goal at top remains the same. Can't wait to see your genius ideas! :)

Target Market(s)

Staff of an elementary school and parents to some (informative) extent as well.

Colors
296eb1
6094c6
fbed22
fbee3f

Requirements
Must have
• items from the white board picture we have attached

```html
<!DOCTYPE html>
<html lang="en">
<head>
<meta charset="utf-8">
<title>Cedar Ridge Elementary – Priority Goal Poster</title>
<link href="https://fonts.googleapis.com/css2?family=Oswald:wght@500;600;700&family=Montserrat:wght@500;600;700;800;900&display=swap" rel="stylesheet">
<style>
  :root{
    --navy:#1e3a7b;
    --blue:#296eb1;
    --blue-soft:#6094c6;
    --yellow:#fbd52a;
    --gold:#efbd12;
    --panel:#e9ebf0;
    --white:#ffffff;
    --stage:#ededed;
  }
  *{box-sizing:border-box;margin:0;padding:0}
  html,body{width:1200px;height:1200px;overflow:hidden;background:var(--stage)}
  .poster{
    position:absolute;left:200px;top:35px;width:800px;height:1130px;
    background:var(--white);overflow:hidden;
    font-family:"Montserrat",sans-serif;
  }
  .goal-title{
    position:absolute;left:24px;top:22px;
    font-weight:900;font-size:35px;letter-spacing:.2px;
    color:var(--navy);
  }
  .goal-title .years{color:var(--gold)}
  .goal-band{
    position:absolute;left:0;top:82px;width:560px;height:98px;
    background:var(--blue);color:var(--white);
    padding:13px 24px;font-weight:600;font-size:16.5px;line-height:1.4;letter-spacing:.4px;
    text-transform:uppercase;
  }
  .school-mark{
    position:absolute;left:580px;top:22px;width:200px;
    display:flex;flex-direction:column;align-items:center;
  }
  .school-mark .dot{width:86px;height:86px;border-radius:50%;background:var(--yellow);margin-bottom:12px}
  .school-mark .name{
    font-weight:800;color:var(--navy);
    font-size:18px;line-height:1.15;text-align:center;text-transform:uppercase;
  }
  .body-panel{position:absolute;left:0;top:195px;width:800px;height:845px;background:var(--panel)}
  .wheel{position:absolute;left:0;top:231px;width:800px;height:800px}
  .wheel text{font-family:"Montserrat",sans-serif;text-anchor:middle}
  .seg-title{font-weight:800;font-size:12px}
  .seg-note{font-weight:500;font-size:8.8px}
  .tagline{font-family:"Oswald",sans-serif !important;font-weight:600}
  .footer-rule{position:absolute;left:0;top:1040px;width:800px;height:8px;background:var(--yellow)}
  .footer{
    position:absolute;left:0;top:1048px;width:800px;height:82px;background:var(--navy);
    color:var(--white);display:flex;align-items:center;justify-content:space-between;padding:0 28px 0 40px;
  }
  .contact{font-weight:600;font-size:15px;line-height:1.45}
  .contact div{display:flex;align-items:center;gap:8px}
  .social{display:flex;align-items:center;gap:12px;font-weight:700;font-size:20px}
  .social .dot{width:30px;height:30px;border-radius:50%;background:var(--blue-soft)}
</style>
</head>
<body>
<main class="poster">
  <header>
    <h1 class="goal-title"><span class="years">2021-2023</span> PRIORITY GOAL</h1>
    <p class="goal-band">We will accelerate the academic and<br>social / emotional growth of each student<br>we serve by deeply focusing on:</p>
    <div class="school-mark">
      <span class="dot"></span>
      <span class="name">Cedar Ridge<br>Elementary School</span>
    </div>
  </header>

  <div class="body-panel"></div>

  <svg class="wheel" viewBox="0 0 800 800" aria-label="Foundational promises wheel">
    <defs>
      <linearGradient id="ringGrad" x1="0" y1="0" x2="1" y2="1">
        <stop offset="0" stop-color="#6094c6"/>
        <stop offset="1" stop-color="#1c2b6b"/>
      </linearGradient>
    </defs>
    <circle cx="400" cy="400" r="334" fill="url(#ringGrad)"/>
    <circle cx="400" cy="400" r="323" fill="#fff"/>
    <path d="M296 114 A303 303 0 1 0 504 114" fill="none" stroke="#6094c6" stroke-width="2"/>

    <!-- yellow segments -->
    <path d="M521.7 139 A288 288 0 0 1 658.3 272.6 L507.6 346.9 A120 120 0 0 0 450.7 291.2Z" fill="#e9b90f"/>
    <path d="M658.3 272.6 A288 288 0 0 1 681.2 462.3 L517.2 426 A120 120 0 0 0 507.6 346.9Z" fill="#f2c923"/>
    <path d="M681.2 462.3 A288 288 0 0 1 580.3 624.6 L475.1 493.6 A120 120 0 0 0 517.2 426Z" fill="#f7dd52"/>
    <path d="M580.3 624.6 A288 288 0 0 1 400 688 L400 520 A120 120 0 0 0 475.1 493.6Z" fill="#f8eba2"/>
    <!-- blue segments -->
    <path d="M400 688 A288 288 0 0 1 219.7 624.6 L324.9 493.6 A120 120 0 0 0 400 520Z" fill="#8db3dc"/>
    <path d="M219.7 624.6 A288 288 0 0 1 118.8 462.3 L282.8 426 A120 120 0 0 0 324.9 493.6Z" fill="#2f6fb8"/>
    <path d="M118.8 462.3 A288 288 0 0 1 141.7 272.6 L292.4 346.9 A120 120 0 0 0 282.8 426Z" fill="#2a47a0"/>
    <path d="M141.7 272.6 A288 288 0 0 1 278.3 139 L349.3 291.2 A120 120 0 0 0 292.4 346.9Z" fill="#1f2f7a"/>

    <!-- top tagline -->
    <text x="400" y="168" class="tagline" font-size="84" fill="#efbd12">5</text>
    <text x="400" y="196" class="tagline" font-size="21" fill="#efbd12">YEARS STRONG</text>
    <text x="400" y="222" class="tagline" font-size="21" fill="#1f3a8a">BETTER</text>
    <text x="400" y="248" class="tagline" font-size="21" fill="#1f3a8a">EVERYDAY!</text>
    <rect x="362" y="256" width="76" height="4" fill="#296eb1"/>

    <!-- centre -->
    <circle cx="400" cy="400" r="122" fill="#dfe9f5"/>
    <circle cx="400" cy="400" r="112" fill="#fff"/>
    <g class="handshake" fill="none" stroke-linecap="round" stroke-linejoin="round">
      <path d="M400 354 C386 334 354 336 354 362 C354 380 374 396 400 418 C426 396 446 380 446 362 C446 336 414 334 400 354Z" stroke="#296eb1" stroke-width="6"/>
      <path d="M366 392 L384 374 L400 378 L412 370 L434 390" stroke="#1e3a7b" stroke-width="3.5"/>
      <path d="M384 374 L404 394 M392 384 L410 402 M400 378 L416 394 M382 392 L398 408" stroke="#1e3a7b" stroke-width="3"/>
    </g>
    <text x="400" y="462" class="tagline" font-size="30" fill="#1e3a7b">FOUNDATIONAL</text>
    <text x="400" y="494" class="tagline" font-size="30" fill="#1e3a7b">PROMISES</text>

    <!-- labels: yellow -->
    <g fill="#1e3a7b">
      <text x="526" y="262" class="seg-title"><tspan x="526">MENTAL HEALTH</tspan><tspan x="526" dy="14">&amp; WELLNESS</tspan></text>
      <text x="526" y="292" class="seg-note"><tspan x="526">For every person in our</tspan><tspan x="526" dy="11">community &amp; school</tspan></text>
      <text x="576" y="360" class="seg-title"><tspan x="576">STAFF DOING</tspan><tspan x="576" dy="14">WHAT THEY</tspan><tspan x="576" dy="14">LOVE</tspan></text>
      <text x="576" y="402" class="seg-note"><tspan x="576">Teaching kids</tspan><tspan x="576" dy="11">for proven growth</tspan></text>
      <text x="552" y="486" class="seg-title">FOCUS</text>
      <text x="552" y="500" class="seg-note"><tspan x="552">Be intentional</tspan><tspan x="552" dy="11">with each action</tspan></text>
      <text x="478" y="548" class="seg-title"><tspan x="478">COMMUNICATE,</tspan><tspan x="478" dy="14">COMMUNICATE,</tspan><tspan x="478" dy="14">COMMUNICATE!</tspan></text>
      <text x="478" y="590" class="seg-note"><tspan x="478">For clarity of understanding,</tspan><tspan x="478" dy="11">expectations and supports</tspan></text>
    </g>
    <!-- labels: blue -->
    <g fill="#fff">
      <text x="322" y="556" class="seg-title"><tspan x="322">BUILD &amp; VALUE</tspan><tspan x="322" dy="14">PARTNERSHIPS</tspan></text>
      <text x="322" y="584" class="seg-note"><tspan x="322">Be predictable, connect,</tspan><tspan x="322" dy="11">celebrate, laugh, have fun!</tspan></text>
      <text x="250" y="478" class="seg-title"><tspan x="250">SMALL</tspan><tspan x="250" dy="14">MEASURED</tspan><tspan x="250" dy="14">STEPS</tspan></text>
      <text x="250" y="518" class="seg-note"><tspan x="250">Towards</tspan><tspan x="250" dy="11">priority goal</tspan></text>
      <text x="222" y="350" class="seg-title"><tspan x="222">BROADEN</tspan><tspan x="222" dy="14">OUR LENS</tspan></text>
      <text x="222" y="378" class="seg-note"><tspan x="222">Appreciating</tspan><tspan x="222" dy="11">each person's</tspan><tspan x="222" dy="11">piece of</tspan><tspan x="222" dy="11">our puzzle</tspan></text>
      <text x="282" y="262" class="seg-title"><tspan x="282">HEARING</tspan><tspan x="282" dy="14">EVERY VOICE</tspan></text>
      <text x="282" y="292" class="seg-note"><tspan x="282">Create sense of</tspan><tspan x="282" dy="11">belonging for all</tspan></text>
    </g>

    <!-- icon badges -->
    <g stroke-width="2.2" fill="none" stroke-linecap="round" stroke-linejoin="round">
      <g transform="translate(587,190)">
        <circle r="28" fill="#fff" stroke="#e9b90f" stroke-width="3"/>
        <path d="M0 -2 C-6 -12 -16 -8 -14 0 C-12 6 -4 10 0 14 C4 10 12 6 14 0 C16 -8 6 -12 0 -2Z" stroke="#1e3a7b"/>
      </g>
      <g transform="translate(672,362)">
        <circle r="28" fill="#fff" stroke="#e9b90f" stroke-width="3"/>
        <circle cy="-7" r="6" stroke="#1e3a7b"/><path d="M-12 14 C-12 2 12 2 12 14Z" stroke="#1e3a7b"/>
      </g>
      <g transform="translate(632,548)">
        <circle r="28" fill="#fff" stroke="#e9b90f" stroke-width="3"/>
        <circle r="12" stroke="#1e3a7b"/><circle r="4" fill="#1e3a7b" stroke="none"/>
        <path d="M0 -18 V-12 M0 12 V18 M-18 0 H-12 M12 0 H18" stroke="#1e3a7b"/>
      </g>
      <g transform="translate(490,660)">
        <circle r="28" fill="#fff" stroke="#e9b90f" stroke-width="3"/>
        <circle cx="-8" cy="-10" r="3.5" stroke="#1e3a7b"/><circle cx="8" cy="-2" r="3.5" stroke="#1e3a7b"/>
        <path d="M-14 2 C-14 -4 -2 -4 -2 2 M2 14 C2 8 14 8 14 14 M-4 -16 H6 V-8 M-6 10 H-14 V4" stroke="#1e3a7b"/>
      </g>
      <g transform="translate(310,660)">
        <circle r="28" fill="#fff" stroke="#6094c6" stroke-width="3"/>
        <circle cx="-9" cy="-2" r="3.5" stroke="#296eb1"/><circle cx="9" cy="-2" r="3.5" stroke="#296eb1"/>
        <path d="M-9 2 V10 L-12 16 M-9 10 L-6 16 M9 2 V10 L6 16 M9 10 L12 16 M-9 4 L-2 -14 M9 4 L2 -14 M-13 4 L-16 10 M13 4 L16 10" stroke="#296eb1"/>
      </g>
      <g transform="translate(168,548)">
        <circle r="28" fill="#fff" stroke="#296eb1" stroke-width="3"/>
        <g fill="#296eb1" stroke="none">
          <path d="M-11 -2 C-15 -2 -16 6 -14 12 C-13 16 -7 16 -7 11 C-7 6 -6 -2 -11 -2Z"/>
          <circle cx="-13" cy="-6" r="1.5"/><circle cx="-10" cy="-7" r="1.5"/><circle cx="-7" cy="-5.5" r="1.4"/>
          <path d="M10 -10 C6 -10 5 -2 7 4 C8 8 14 8 14 3 C14 -2 15 -10 10 -10Z"/>
          <circle cx="7" cy="-14" r="1.4"/><circle cx="10" cy="-15" r="1.5"/><circle cx="13" cy="-13.5" r="1.5"/>
        </g>
      </g>
      <g transform="translate(128,362)">
        <circle r="28" fill="#fff" stroke="#2a47a0" stroke-width="3"/>
        <path d="M-15 0 C-8 -10 8 -10 15 0 C8 10 -8 10 -15 0Z" stroke="#1e3a7b"/>
        <circle r="4" fill="#1e3a7b" stroke="none"/>
      </g>
      <g transform="translate(213,190)">
        <circle r="28" fill="#fff" stroke="#1f2f7a" stroke-width="3"/>
        <circle cx="-9" cy="-7" r="4" stroke="#1e3a7b"/><circle cx="9" cy="-7" r="4" stroke="#1e3a7b"/><circle cy="-3" r="4" stroke="#1e3a7b"/>
        <path d="M-15 12 V2 H-3 M15 12 V2 H3 M-5 14 V6 H5 V14" stroke="#1e3a7b"/>
      </g>
    </g>
  </svg>

  <div class="footer-rule"></div>
  <footer class="footer">
    <div class="contact">
      <div><svg width="14" height="16" viewBox="0 0 14 16"><path d="M7 0 C3 0 0 3 0 6.5 C0 11 7 16 7 16 C7 16 14 11 14 6.5 C14 3 11 0 7 0Z" fill="#fbd52a"/><circle cx="7" cy="6.5" r="2.5" fill="#1e3a7b"/></svg>1820 Alder Grove Rd., Pine Hollow, WA 98000</div>
      <div><svg width="14" height="14" viewBox="0 0 14 14"><path d="M3 0 L5.5 3.5 L4 5.5 C5 7.5 6.5 9 8.5 10 L10.5 8.5 L14 11 L12 14 C6 14 0 8 0 2Z" fill="#fbd52a"/></svg>555-014-2200</div>
    </div>
    <div class="social"><span class="dot"></span>@cedarridgelearns</div>
  </footer>
</main>
</body>
</html>
```